Help us make a TAILWARDLY impact! Saving Dogs from Kill Shelters.....

*Our mission is to save Dogs from kill shelters, and unite them with responsible families nationwide.

*We would love to incorporate sacred geometry into our message. The "Flower of Life" needs to be incorporated into this design.Earth Friendly Self-Sustainable Animal Shelter is a goal. Solar Power

*We want the professional look of exclusiveness.

*The logo/brand is not set in stone, and we welcome opinions!

***Earth Consciousness. Awareness. Love.

Peace. LOVE. Adopt. :)

I would like a sleek exclusive look, one that says WOW. This design needs to have a good energy about it. I have envisioned the front being logo only and vertical. Please have a look at our Chatterbook page to get a feel about what we are doing & trying to accomplish...

*ONE Side Card
**The flower of life inlay needs to be in or around of the logo.
***The following is the ONLY information I want on the card!

TAILWARDLY Adoption Center

Marisol Dunkett

www.TAILWARDLYadoptionhub-example.com

(555)013-8764

CB Icon

Target Market(s)

Stable, Wealthy, Responsible Families in the Northeast.

Industry/Entity Type

Solar

Contact Information for Business Card

TAILWARDLY Adoption Center, Marisol Dunkett, Founder/Director, 712 Quillfern Court, Bath Springs, TN 00000, (555)013-8764, CB Icon

Requirements
Must have
• CB icon on back.
The "Flower of Life" must be incorporated into this design.
Nice to have
• Positive Energy
Bright Colors
WOW Factor

```html
<!DOCTYPE html>
<html lang="en">
<head>
<meta charset="utf-8">
<title>TAILWARDLY Adoption Centre – Business Card</title>
<link rel="stylesheet" href="https://fonts.googleapis.com/css2?family=Arimo:wght@400;700&display=swap">
<style>
  :root {
    --page-bg: #e9ebe6;
    --card-bg: #ffffff;
    --lime: #9cc93c;
    --lime-light: #b6d85a;
    --forest: #3f8a2c;
    --ink: #1d1d1d;
    --ink-soft: #333333;
    --white: #ffffff;
  }
  * { box-sizing: border-box; margin: 0; padding: 0; }
  html, body {
    width: 1200px;
    height: 1200px;
    overflow: hidden;
    background: var(--page-bg);
    font-family: "Arimo", Arial, sans-serif;
  }
  .canvas {
    position: relative;
    width: 1200px;
    height: 1200px;
  }
  .business-card {
    position: absolute;
    left: 300px;
    top: 75px;
    width: 600px;
    height: 1050px;
    background: var(--card-bg);
    box-shadow: 0 6px 24px rgba(0,0,0,0.12);
    overflow: hidden;
  }
  .frame {
    position: absolute;
    border: 2px solid var(--lime);
    border-bottom: none;
  }
  .frame--outer { left: 18px; right: 18px; top: 18px; height: 812px; }
  .frame--inner { left: 30px; right: 30px; top: 30px; height: 800px; }

  .brand {
    position: absolute;
    top: 70px;
    left: 0;
    right: 0;
    text-align: center;
  }
  .brand-mark {
    display: block;
    width: 170px;
    height: 170px;
    margin: 0 auto 34px;
    border-radius: 50%;
    background: radial-gradient(circle at 40% 38%, var(--lime-light), var(--forest));
  }
  .brand-name {
    font-weight: 700;
    font-size: 40px;
    letter-spacing: 1px;
    color: var(--lime);
    line-height: 1;
  }
  .brand-tagline {
    margin-top: 8px;
    font-size: 24px;
    color: var(--lime);
  }
  .divider {
    position: absolute;
    top: 420px;
    left: 30px;
    right: 30px;
    height: 3px;
    background: linear-gradient(90deg, var(--forest), var(--lime));
  }
  .contact {
    position: absolute;
    top: 470px;
    left: 0;
    right: 0;
    text-align: center;
    color: var(--ink);
  }
  .contact-name { font-weight: 700; font-size: 34px; }
  .contact-role { margin-top: 10px; font-size: 18px; color: var(--ink-soft); }
  .contact-web { margin-top: 62px; font-size: 22px; }
  .contact-phone { margin-top: 40px; font-size: 27px; letter-spacing: 1px; }

  .social-band {
    position: absolute;
    left: 0;
    right: 0;
    bottom: 0;
    height: 220px;
    background: var(--lime);
    display: flex;
    align-items: center;
    justify-content: center;
  }
  .social-name {
    color: var(--white);
    font-weight: 700;
    font-size: 32px;
  }
</style>
</head>
<body>
  <main class="canvas">
    <article class="business-card">
      <div class="frame frame--outer"></div>
      <div class="frame frame--inner"></div>

      <header class="brand">
        <span class="brand-mark" aria-hidden="true"></span>
        <h1 class="brand-name">TAILWARDLY</h1>
        <p class="brand-tagline">Adoption Centre</p>
      </header>

      <div class="divider"></div>

      <section class="contact">
        <p class="contact-name">Marisol Dunkett</p>
        <p class="contact-role">Founder</p>
        <p class="contact-web">www.TAILWARDLYadoptionhub-example.com</p>
        <p class="contact-phone">(555) 013 8764</p>
      </section>

      <footer class="social-band">
        <span class="social-name">Chatterbook</span>
      </footer>
    </article>
  </main>
</body>
</html>
```